Simple Website Design for Law Office

I need a website design for our law office (Law Offices of Marcus Pellow) that is extremely simple, only including a landing page and perhaps a contact page (parallax scrolling).

Website should look similar to this one (template): https://www.brightfenwaystudio.com/

Design should be modern, simple, and inviting. There are a few assets like logo, stock photos/icons we would like added as well, and some language and contact info, but very basic stuff.

The name of the company is: Law Offices of Marcus Pellow

Target Market(s)

B2B corporate clients, users from Canada, UK, East Asia, and all potential users with immigration needs

Coding

Coded - Design and coding required

Number of Pages Required

2 page

Colors

Designer to choose colors to be used in the design.

Requirements
Must have
• Landing page, Contact Page
• Simple, elegant design with minimalist font
Nice to have
• Parallax scrolling, so one page and can scroll to contact us segment

```html
<!DOCTYPE html>
<html lang="en">
<head>
<meta charset="utf-8">
<title>Law Offices of Marcus Pellow</title>
<link href="https://fonts.googleapis.com/css2?family=Montserrat:wght@600;700&family=Roboto:ital,wght@0,400;0,500;0,700;1,400&display=swap" rel="stylesheet">
<style>
:root{
  --gold:#d4a452;
  --gold-soft:#dcb877;
  --ink:#222;
  --text:#555;
  --nav:#3a3a3a;
  --grey:#f2f2f2;
  --line:#e2e2e2;
}
*{box-sizing:border-box;margin:0;padding:0}
html,body{width:1200px;height:3195px;overflow:hidden;background:#fff}
body{font-family:'Roboto',sans-serif;color:var(--text);font-size:15px;position:relative}
.head{font-family:'Montserrat',sans-serif;font-weight:700;color:var(--ink);text-transform:uppercase}
.abs{position:absolute}

/* top bar */
.topbar{position:absolute;top:0;left:0;width:1200px;height:94px;background:#fff}
.brand{left:110px;top:36px;font-size:23px}
.top-items{position:absolute;right:110px;top:18px;display:flex;height:58px}
.top-item{padding:0 10px;border-left:1px solid var(--line);text-align:center;display:flex;flex-direction:column;justify-content:center}
.top-item .big{font-size:18px;font-weight:500;color:var(--ink);display:flex;align-items:center;gap:8px;justify-content:center}
.top-item small{font-size:13px;color:var(--text);margin-top:4px}
.top-item .ic{font-size:12px;font-weight:700;color:var(--ink)}

/* nav */
.nav{position:absolute;top:94px;left:0;width:1200px;height:43px;background:var(--nav);display:flex;align-items:center;padding:0 110px}
.nav a{color:#fff;text-decoration:none;font-size:15px;font-weight:500;text-transform:uppercase;margin-right:35px;position:relative}
.nav a.active{color:var(--gold)}
.nav a.active::before{content:"";position:absolute;left:-2px;right:-2px;top:-16px;height:4px;background:var(--gold)}
.nav .lang{color:#fff;font-size:14px;font-weight:500}
.btn{display:inline-block;background:var(--gold);color:var(--ink);font-weight:700;font-size:15px;text-transform:uppercase;border-radius:30px;text-decoration:none}
.nav .btn{margin-left:auto;margin-right:0;padding:8px 12px;color:var(--ink)}

/* hero */
.hero{position:absolute;top:137px;left:0;width:1200px;height:470px;background:linear-gradient(180deg,#5b3f6e 0%,#7a5a86 25%,#3e4a7a 55%,#1d2340 80%,#2c3152 100%);text-align:center;color:#fff}
.hero h1{font-family:'Montserrat',sans-serif;font-size:44px;margin-top:128px;letter-spacing:1px;text-shadow:0 2px 4px rgba(0,0,0,.4)}
.hero p{font-size:18px;line-height:28px;margin-top:14px;text-shadow:0 1px 3px rgba(0,0,0,.5)}
.hero .btn{margin-top:28px;padding:15px 27px;font-size:16px}

/* about */
.photo-frame-a{left:126px;top:676px;width:146px;height:166px;border-top:5px solid var(--gold);border-left:5px solid var(--gold)}
.photo-frame-b{left:372px;top:968px;width:146px;height:166px;border-bottom:5px solid var(--gold);border-right:5px solid var(--gold)}
.photo{left:135px;top:685px;width:374px;height:441px;background:linear-gradient(160deg,#6f7f78,#4c5a58 60%,#2a2a30)}
.about{left:600px;top:700px;width:480px}
.about h2{font-size:34px;margin-bottom:20px}
.job h3{font-size:19px;font-weight:500;color:var(--ink);margin-left:2px}
.job .co{font-size:16px;color:var(--ink);margin-top:4px}
.job .date{font-size:15px;font-style:italic;color:#777;margin-top:8px;display:flex;align-items:center;gap:8px}
.ticks{list-style:none}
.ticks li{position:relative;padding-left:30px;line-height:25px;font-size:15px;margin-top:12px}
.ticks li svg{position:absolute;left:0;top:5px}
.about .btn{padding:11px 20px;font-size:15px;margin-top:26px;display:inline-flex;align-items:center;gap:8px}

/* practice */
.band{position:absolute;left:0;width:1200px}
.band .txt{position:absolute;width:600px;height:100%;background:var(--grey)}
.band .img{position:absolute;width:600px;height:100%}
.band h2{font-size:26px;margin-bottom:22px}
.band .inner{position:absolute}

/* contact */
.contact-title{top:2352px;left:0;width:1200px;text-align:center;font-size:35px}
.cbox{position:absolute;top:2410px;width:314px;height:67px;background:var(--gold);display:flex}
.cbox .ico{width:56px;background:var(--nav);display:flex;align-items:center;justify-content:center}
.cbox .body{padding:0 18px;display:flex;align-items:center;color:var(--ink)}
.map{left:111px;top:2508px;width:977px;height:410px;background:linear-gradient(135deg,#dcdcdc,#cfcfcf 50%,#d8d8d8)}
.form{left:559px;top:2546px;width:516px;height:346px;background:rgba(214,176,105,.88);padding:24px 20px}
.form h4{text-align:center;font-size:18px;font-weight:500;color:var(--ink);text-transform:uppercase}
.field{background:#fff;height:38px;font-size:14px;color:var(--text);padding:10px 18px}
.row{display:flex;gap:8px;margin-top:10px}
.row .field{flex:1}
.form .btn{display:block;margin:18px auto 0;width:96px;text-align:center;padding:7px 0;font-size:15px}

/* footer */
.foot-band{top:2993px;left:0;width:1200px;height:54px;background:var(--gold);display:flex;align-items:center;padding:0 110px}
.foot-band .brand-f{font-size:19px}
.foot-links{margin-left:auto;margin-right:165px;display:flex;gap:0;font-size:15px;font-weight:500;color:var(--ink)}
.foot-links span{padding:0 14px}
.disclaimer{top:3077px;left:0;width:1200px;text-align:center;font-size:16px;line-height:25px}
.copy{top:3150px;left:0;width:1200px;text-align:center;font-size:15px}
</style>
</head>
<body>

<header class="topbar">
  <div class="abs head brand">Marcus Pellow</div>
  <div class="top-items">
    <div class="top-item">
      <div class="big"><svg width="18" height="18" viewBox="0 0 18 18"><circle cx="9" cy="9" r="7.5" fill="none" stroke="#d4a452" stroke-width="2"/><path d="M9 4.5V9l3 2" fill="none" stroke="#d4a452" stroke-width="2"/></svg>09:00 - 17:00</div>
      <small>Opening Hours Mon-Fri</small>
    </div>
    <div class="top-item">
      <div class="big"><svg width="20" height="18" viewBox="0 0 20 18"><path d="M3 10V9a7 7 0 0 1 14 0v1" fill="none" stroke="#d4a452" stroke-width="2"/><rect x="2" y="9" width="4" height="6" rx="1" fill="#d4a452"/><rect x="14" y="9" width="4" height="6" rx="1" fill="#d4a452"/></svg>(415) 555-0142</div>
      <small>Call Us For Free Consultation</small>
    </div>
    <div class="top-item"><div class="ic">•</div><small>Network</small></div>
    <div class="top-item"><div class="ic">•</div><small>Updates</small></div>
    <div class="top-item"><div class="big"><svg width="14" height="14" viewBox="0 0 14 14"><circle cx="8" cy="6" r="4" fill="none" stroke="#222" stroke-width="2"/><path d="M5 9l-3.5 3.5" stroke="#222" stroke-width="2"/></svg></div><small>Search</small></div>
  </div>
</header>

<nav class="nav">
  <a class="active" href="#">Home</a>
  <a href="#">Marcus Pellow</a>
  <a href="#">Our Services</a>
  <a href="#">Contact Us</a>
  <span class="lang">Eng ▾</span>
  <a class="btn" href="#">Contact Us Today</a>
</nav>

<section class="hero" role="img" aria-label="City skyline at dusk reflected on water">
  <h1>MARCUS PELLOW LAW</h1>
  <p>Lorem ipsum dolor sit amet, consectetur adipiscing elit, sed do<br>eiusmod tempor incididunt ut labore et magna aliqua.</p>
  <a class="btn" href="#">Free Consultation</a>
</section>

<div class="abs photo-frame-a"></div>
<div class="abs photo-frame-b"></div>
<div class="abs photo" role="img" aria-label="Portrait of the attorney in a dark suit"></div>

<section class="abs about">
  <h2 class="head">Marcus Pellow</h2>
  <div class="job">
    <h3>Attorney</h3>
    <div class="co">Law Offices of Marcus Pellow</div>
    <div class="date"><svg width="14" height="14" viewBox="0 0 14 14"><rect x="1" y="2" width="12" height="11" fill="none" stroke="#d4a452" stroke-width="1.5"/><path d="M1 5h12" stroke="#d4a452" stroke-width="1.5"/></svg>Jun 2013 – Present</div>
    <ul class="ticks"><li><svg width="14" height="14" viewBox="0 0 14 14"><circle cx="7" cy="7" r="7" fill="#3a5a5a"/><path d="M4 7l2 2 4-4" fill="none" stroke="#fff" stroke-width="1.6"/></svg>Handle all clients needs including criminal, transactional, and general civil litigation: personal injury, wrongful foreclosure/loan modification, breach of contract.</li></ul>
  </div>
  <div class="job" style="margin-top:20px">
    <h3>Appearance Attorney</h3>
    <div class="co">Halvern Law Group</div>
    <div class="date"><svg width="14" height="14" viewBox="0 0 14 14"><rect x="1" y="2" width="12" height="11" fill="none" stroke="#d4a452" stroke-width="1.5"/><path d="M1 5h12" stroke="#d4a452" stroke-width="1.5"/></svg>Jan 2013 – Present</div>
    <ul class="ticks"><li><svg width="14" height="14" viewBox="0 0 14 14"><circle cx="7" cy="7" r="7" fill="#3a5a5a"/><path d="M4 7l2 2 4-4" fill="none" stroke="#fff" stroke-width="1.6"/></svg>Appear in superior court for criminal cases regarding arraignments, continuances, and entering of pleas.</li></ul>
  </div>
  <a class="btn" href="#">Load More <svg width="14" height="14" viewBox="0 0 14 14"><circle cx="7" cy="7" r="7" fill="#222"/><path d="M4 6l3 3 3-3" fill="none" stroke="#d4a452" stroke-width="1.8"/></svg></a>
</section>

<!-- Foreclosure -->
<section class="band" style="top:1231px;height:391px">
  <div class="txt" style="left:0"></div>
  <div class="img" style="left:600px;background:linear-gradient(180deg,#2f5fa8 0%,#6a8fc4 30%,#b49a6e 55%,#a58f74 100%)" role="img" aria-label="Suburban two-storey house with driveway"></div>
  <div class="inner" style="left:110px;top:42px;width:470px">
    <h2 class="head">Foreclosure / HBOR</h2>
    <ul class="ticks">
      <li><svg width="14" height="14" viewBox="0 0 14 14"><circle cx="7" cy="7" r="7" fill="#d4a452"/><path d="M4 7l2 2 4-4" fill="none" stroke="#fff" stroke-width="1.6"/></svg>$1,880,000 settlement for loan servicer’s wrongful foreclosure, wrongful eviction, conversion, and reckless mishandling of loan modification. Servicer conceded after five years of litigation and days before trial.</li>
      <li><svg width="14" height="14" viewBox="0 0 14 14"><circle cx="7" cy="7" r="7" fill="#d4a452"/><path d="M4 7l2 2 4-4" fill="none" stroke="#fff" stroke-width="1.6"/></svg>$300,000 settlement for reduction in principle mortgage balance for loan servicer’s grossly negligent handling of loan modification application.</li>
      <li><svg width="14" height="14" viewBox="0 0 14 14"><circle cx="7" cy="7" r="7" fill="#d4a452"/><path d="M4 7l2 2 4-4" fill="none" stroke="#fff" stroke-width="1.6"/></svg>$40,000.00 in attorneys fees and costs awarded by the court in conjunction with preliminary injunction of pending trustee’s sale.</li>
    </ul>
  </div>
</section>

<!-- Personal injury -->
<section class="band" style="top:1622px;height:352px">
  <div class="img" style="left:0;background:linear-gradient(120deg,#2d3e52 0%,#3b4e63 45%,#b89a84 60%,#5a6a45 100%)" role="img" aria-label="Person holding a wrist in a support brace"></div>
  <div class="inner" style="left:619px;top:60px;width:475px">
    <h2 class="head">Personal Injury / Insurance</h2>
    <ul class="ticks">
      <li><svg width="14" height="14" viewBox="0 0 14 14"><circle cx="7" cy="7" r="7" fill="#d4a452"/><path d="M4 7l2 2 4-4" fill="none" stroke="#fff" stroke-width="1.6"/></svg>$100,000 for damage to commercial property after carrier’s initial denial to extend coverage under client’s policy.</li>
      <li><svg width="14" height="14" viewBox="0 0 14 14"><circle cx="7" cy="7" r="7" fill="#d4a452"/><path d="M4 7l2 2 4-4" fill="none" stroke="#fff" stroke-width="1.6"/></svg>$75,000 settlement for violent dog bite incident when prior counsel mishandled file and initial stages of litigation.</li>
      <li><svg width="14" height="14" viewBox="0 0 14 14"><circle cx="7" cy="7" r="7" fill="#d4a452"/><path d="M4 7l2 2 4-4" fill="none" stroke="#fff" stroke-width="1.6"/></svg>$35,000 in damages to vehicle after multiple denials by carrier to extend coverage.</li>
    </ul>
  </div>
</section>

<!-- Criminal -->
<section class="band" style="top:1974px;height:306px">
  <div class="txt" style="left:0"></div>
  <div class="img" style="left:600px;background:linear-gradient(90deg,#1e1f22 0%,#2b2d31 40%,#c8542a 60%,#3a3733 85%,#2a2826 100%)" role="img" aria-label="Officer escorting a person in an orange jumpsuit"></div>
  <div class="inner" style="left:110px;top:56px;width:470px">
    <h2 class="head">Criminal</h2>
    <ul class="ticks">
      <li><svg width="14" height="14" viewBox="0 0 14 14"><circle cx="7" cy="7" r="7" fill="#d4a452"/><path d="M4 7l2 2 4-4" fill="none" stroke="#fff" stroke-width="1.6"/></svg>Domestic violence charges dismissed prior to jury selection.</li>
      <li style="margin-top:20px"><svg width="14" height="14" viewBox="0 0 14 14"><circle cx="7" cy="7" r="7" fill="#d4a452"/><path d="M4 7l2 2 4-4" fill="none" stroke="#fff" stroke-width="1.6"/></svg>Drug sales charges referred to drug court and charges expunged.</li>
      <li style="margin-top:18px"><svg width="14" height="14" viewBox="0 0 14 14"><circle cx="7" cy="7" r="7" fill="#d4a452"/><path d="M4 7l2 2 4-4" fill="none" stroke="#fff" stroke-width="1.6"/></svg>.21 BAC DUI charges dismissed pursuant to successful suppression hearing.</li>
    </ul>
  </div>
</section>

<!-- Contact -->
<h2 class="abs head contact-title">Contact Us</h2>

<div class="cbox" style="left:111px">
  <div class="ico"><svg width="16" height="22" viewBox="0 0 16 22"><path d="M8 0a8 8 0 0 1 8 8c0 6-8 14-8 14S0 14 0 8a8 8 0 0 1 8-8z" fill="#fff"/><circle cx="8" cy="8" r="3" fill="#3a3a3a"/></svg></div>
  <div class="body" style="font-size:13px;line-height:20px">Law Offices of Marcus Pellow 2210 Alder Park Ave., 4th Floor Westbrook, CA 91580</div>
</div>
<div class="cbox" style="left:443px">
  <div class="ico"><svg width="22" height="22" viewBox="0 0 22 22"><path d="M5 1l4 5-2.5 2.5a12 12 0 0 0 7 7L16 13l5 4-2.5 3.5C10 20 2 12 1.5 3.5z" fill="#fff"/></svg></div>
  <div class="body" style="font-size:17px;font-weight:500;line-height:28px">Tel: (415) 555-0142<br>Fax: (415) 555-0178</div>
</div>
<div class="cbox" style="left:775px">
  <div class="ico"><svg width="24" height="18" viewBox="0 0 24 18"><rect width="24" height="18" rx="2" fill="#fff"/><path d="M1 2l11 8 11-8" fill="none" stroke="#3a3a3a" stroke-width="2"/></svg></div>
  <div class="body" style="font-size:16px;padding-left:18px">marcuspellowlaw@mail.com</div>
</div>

<div class="abs map" role="img" aria-label="Street map showing the office location"></div>
<form class="abs form">
  <h4>Get in Touch</h4>
  <div class="row" style="margin-top:24px"><div class="field">First Name</div><div class="field">Last Name</div></div>
  <div class="row"><div class="field">Email</div><div class="field">phone number</div></div>
  <div class="row"><div class="field" style="height:74px">Message</div></div>
  <span class="btn">Submit</span>
</form>

<footer>
  <div class="abs foot-band">
    <span class="head brand-f">Marcus Pellow</span>
    <div class="foot-links"><span>HOME</span><span>|</span><span>MARCUS PELLOW</span><span>|</span><span>OUR SERVICES</span><span>|</span><span>CONTACT US</span></div>
  </div>
  <p class="abs disclaimer">The information presented in this website should not be construed to be formal legal advice nor the formation of a lawyer/client<br>relationship. Persons accessing this site are encouraged to seek independent counsel for advice regarding their individual legal issues.</p>
  <p class="abs copy">© 2019 Law Offices of Marcus Pellow. All rights reserved.</p>
</footer>

</body>
</html>
```